Business card

We are looking for a creative person to deigns our company business card.

Target Market(s)

College age student

Industry/Entity Type

Accommodation

Contact Information for Business Card

We want a fun, clean and sophisticated design. It should look good, but more importantly the information should be legible.

Font styles to use
Serif
Sans Serif
Other font styles liked:
• Open Sans ,

Colors
33a6d7

Requirements
Must have
• Must have a young and memorable message. Be legible.
• Our logo on the back on a solid blue , please find color and logo attached
• LodgeNestly.com on the back.
Nice to have
• I would like to have couple of different fonts on the LodgeNestly.com on the back of the cards with a solid blue.

```html
<!DOCTYPE html>
<html lang="en">
<head>
<meta charset="utf-8">
<title>LodgeNestly Business Card</title>
<link rel="stylesheet" href="https://fonts.googleapis.com/css2?family=Cinzel:wght@400&family=Open+Sans:wght@300;400;700&display=swap">
<style>
  :root {
    --brand-blue: #33a6d7;
    --deep-navy: #1c3761;
    --name-navy: #23446f;
    --link-blue: #2f7fc1;
    --paper: #fbfbfa;
    --backdrop: #e9ecef;
    --white: #ffffff;
  }
  * { margin: 0; padding: 0; box-sizing: border-box; }
  html, body { width: 1200px; height: 800px; overflow: hidden; }
  body {
    background: var(--backdrop);
    font-family: "Open Sans", Arial, sans-serif;
    position: relative;
  }
  .card {
    position: absolute;
    top: 246px;
    width: 540px;
    height: 308px;
    border-radius: 4px;
    box-shadow: 0 6px 20px rgba(20, 40, 70, 0.18);
    overflow: hidden;
  }
  .card-front { left: 40px; background: var(--paper); }
  .card-back { left: 620px; background: var(--brand-blue); }

  .holder-name {
    position: absolute;
    left: 52px;
    top: 46px;
    font-family: "Cinzel", Georgia, serif;
    font-size: 33px;
    letter-spacing: 1px;
    color: var(--name-navy);
    line-height: 1;
  }
  .holder-role {
    position: absolute;
    right: 212px;
    top: 86px;
    font-size: 12px;
    color: #4a5a70;
  }
  .contact-list {
    position: absolute;
    right: 192px;
    top: 112px;
    list-style: none;
  }
  .contact-item {
    display: flex;
    justify-content: flex-end;
    align-items: center;
    gap: 12px;
    height: 25px;
    font-size: 14.5px;
    color: var(--link-blue);
  }
  .contact-icon { width: 13px; height: 13px; fill: var(--deep-navy); flex: none; }

  .brand-front {
    position: absolute;
    left: 362px;
    top: 112px;
    width: 160px;
    display: flex;
    flex-direction: column;
    align-items: center;
    gap: 12px;
  }
  .brand-square { width: 26px; height: 26px; background: var(--deep-navy); }
  .brand-name {
    font-weight: 700;
    font-size: 22px;
    color: var(--deep-navy);
    letter-spacing: -0.3px;
  }

  .front-bands { position: absolute; left: 0; top: 0; }
  .address-line {
    position: absolute;
    left: 40px;
    top: 276px;
    font-size: 9px;
    color: var(--white);
    letter-spacing: 0.2px;
  }

  .brand-back {
    position: absolute;
    left: 0;
    right: 0;
    top: 92px;
    display: flex;
    flex-direction: column;
    align-items: center;
    gap: 14px;
  }
  .brand-back .brand-square { background: var(--white); width: 30px; height: 30px; }
  .brand-back .brand-name { color: var(--white); font-size: 30px; }
  .site-line {
    font-weight: 300;
    font-size: 22px;
    letter-spacing: 1px;
    color: var(--white);
  }
</style>
</head>
<body>

  <section class="card card-front" aria-label="Business card front">
    <svg class="front-bands" width="540" height="308" viewBox="0 0 540 308" aria-hidden="true">
      <polygon points="0,268 318,268 330,292 0,292" fill="var(--brand-blue)"/>
      <polygon points="318,252 540,240 540,252 332,264" fill="var(--deep-navy)"/>
    </svg>

    <h1 class="holder-name">Marcus Hale</h1>
    <p class="holder-role">Manager</p>

    <ul class="contact-list">
      <li class="contact-item">555-204-1187
        <svg class="contact-icon" viewBox="0 0 16 16" aria-label="Fax"><rect x="4" y="1" width="8" height="4"/><rect x="1" y="6" width="14" height="6" rx="1"/><rect x="4" y="10" width="8" height="5"/></svg>
      </li>
      <li class="contact-item">555-204-1188
        <svg class="contact-icon" viewBox="0 0 16 16" aria-label="Phone"><path d="M3 1l3 0 1 4-2 1.5c1 2 2.5 3.5 4.5 4.5L11 9l4 1v3c0 1-1 2-2 2C7 15 1 9 1 3c0-1 1-2 2-2z"/></svg>
      </li>
      <li class="contact-item">marcus@lodgenestly.com
        <svg class="contact-icon" viewBox="0 0 16 16" aria-label="Email"><path d="M1 3h14v10H1z M1 3l7 6 7-6" fill="none" stroke="var(--deep-navy)" stroke-width="1.6"/></svg>
      </li>
      <li class="contact-item">LodgeNestly.com
        <svg class="contact-icon" viewBox="0 0 16 16" aria-label="Website"><circle cx="8" cy="8" r="6.5" fill="none" stroke="var(--deep-navy)" stroke-width="1.5"/><ellipse cx="8" cy="8" rx="2.6" ry="6.5" fill="none" stroke="var(--deep-navy)" stroke-width="1.2"/><line x1="1.5" y1="8" x2="14.5" y2="8" stroke="var(--deep-navy)" stroke-width="1.2"/></svg>
      </li>
    </ul>

    <div class="brand-front">
      <span class="brand-square" aria-hidden="true"></span>
      <span class="brand-name">LodgeNestly</span>
    </div>

    <p class="address-line">88 Harbor Lane, Suite 210, Portland, Oregon OR 97205</p>
  </section>

  <section class="card card-back" aria-label="Business card back">
    <div class="brand-back">
      <span class="brand-square" aria-hidden="true"></span>
      <span class="brand-name">LodgeNestly</span>
      <span class="site-line">LodgeNestly.com</span>
    </div>
  </section>

</body>
</html>
```